Business Card Design Project for Investment Fund

Veloria Capital Management is an emerging wealth management firm based in New Jersey. It offers superior investment returns to high net worth individuals and institutions by finding undervalued assets.
We recently selected a company logo which was inspired by the Tucana constellation. Beta Tucanae is a group of six stars, containing star cluster 47 Tucanae, rated the second brightest object in the sky.
Now we need a business card design. Since we are an investment firm, the design should project a sense of stability, growth and professionalism. The owner is interested in something simple yet striking, which of course is consistent with the logo.
Wealthy individuals, probably middle aged or older, in the US
Investment

```html
<!DOCTYPE html>
<html lang="en">
<head>
<meta charset="utf-8">
<title>Veloria Capital Management – Business Card</title>
<link rel="stylesheet" href="https://fonts.googleapis.com/css2?family=Mulish:wght@400;600;700&family=Roboto+Condensed:wght@400;700&display=swap">
<style>
  :root {
    --paper: #ffffff;
    --ink: #111111;
    --slate: #2b3742;
    --night: #1b1d4e;
    --night-deep: #15163f;
    --night-light: #26296a;
    --brand-blue: #1f3fae;
  }
  * { margin: 0; padding: 0; box-sizing: border-box; }
  html, body {
    width: 1200px;
    height: 741px;
    overflow: hidden;
    background: var(--paper);
  }
  .card {
    position: relative;
    width: 1200px;
    height: 741px;
    background: var(--paper);
    font-family: "Mulish", sans-serif;
    color: var(--ink);
  }
  .night-band {
    position: absolute;
    left: 539px;
    top: 0;
    width: 349px;
    height: 741px;
    background:
      radial-gradient(ellipse at 45% 40%, var(--night-light) 0%, transparent 60%),
      linear-gradient(180deg, var(--night) 0%, var(--night-deep) 100%);
  }
  .contact {
    position: absolute;
    left: 0;
    width: 532px;
    top: 252px;
    text-align: center;
    font-weight: 700;
  }
  .contact .address {
    font-size: 27px;
    line-height: 36px;
  }
  .contact .phone {
    margin-top: 10px;
    font-size: 27px;
    line-height: 36px;
    display: flex;
    justify-content: center;
    align-items: center;
    gap: 8px;
  }
  .contact .phone svg { width: 34px; height: 34px; }
  .contact .email,
  .contact .web {
    font-size: 24.5px;
    line-height: 32px;
  }
  .contact .email { margin-top: 9px; }
  .contact .web { margin-top: 9px; }
  .brand {
    position: absolute;
    left: 925px;
    width: 250px;
    top: 70px;
    text-align: center;
    color: var(--slate);
    font-weight: 600;
  }
  .brand .mark {
    display: block;
    width: 96px;
    height: 96px;
    margin: 0 auto 12px;
    border-radius: 12px;
    background: var(--brand-blue);
  }
  .brand .name-main {
    font-size: 34px;
    letter-spacing: 4px;
    line-height: 38px;
    text-transform: uppercase;
  }
  .brand .name-sub {
    font-size: 18px;
    line-height: 24px;
  }
  .person {
    position: absolute;
    left: 925px;
    width: 250px;
    top: 578px;
    text-align: center;
    font-family: "Roboto Condensed", sans-serif;
  }
  .person .name {
    font-size: 41px;
    font-weight: 700;
    line-height: 46px;
  }
  .person .role {
    font-size: 28px;
    font-weight: 400;
    line-height: 34px;
  }
</style>
</head>
<body>
  <div class="card">
    <div class="contact">
      <p class="address">48 Halden St.<br>New York, NY 10001</p>
      <p class="phone">
        <svg viewBox="0 0 34 34" aria-hidden="true">
          <circle cx="17" cy="17" r="15" fill="none" stroke="#111" stroke-width="2"/>
          <path d="M11.5 9.5 l3 -1 l2 4.5 l-2 1.5 c1 2.5 2.5 4 5 5 l1.5 -2 l4.5 2 l-1 3 c-6 1 -13 -6 -13 -13 z" fill="#111"/>
        </svg>
        (212) 555-0148
      </p>
      <p class="email">dharrow@veloriacapital.com</p>
      <p class="web">www.veloriacapital.com</p>
    </div>

    <div class="night-band" role="img" aria-label="Starry night sky field of scattered white stars"></div>

    <div class="brand">
      <span class="mark" aria-hidden="true"></span>
      <p class="name-main">Veloria</p>
      <p class="name-sub">Capital Management</p>
    </div>

    <div class="person">
      <p class="name">Daniel Harrow</p>
      <p class="role">CEO</p>
    </div>
  </div>
</body>
</html>
```